Redesign existing website

We would like a redesign of the website http://www.vastelquery.com that creates a more modern, up to date look.

Vastel Query creates software for social science research and is focused on making the software user friendly and easy to use. We would like to convey seriousness, but also
a very up to date, just released look.

Feel free to modify the logo if you wish.

Target Market(s)

Academics, researchers

Industry/Entity Type

Software

Requirements
Must have
• The design should incorporate the same information as the current website.

```html
<!DOCTYPE html>
<html lang="en">
<head>
<meta charset="utf-8">
<title>Vastel Query – Home</title>
<link rel="stylesheet" href="https://fonts.googleapis.com/css2?family=Arimo:wght@400;700&family=Gelasio:ital,wght@0,400;0,700;1,400&display=swap">
<style>
:root{
  --blue:#1f3f9a;
  --blue-deep:#1a3a8f;
  --blue-hero:#233f9c;
  --nav-top:#2fa8ea;
  --nav-bottom:#1377c9;
  --gray-band:#a9a9a9;
  --text:#333;
  --muted:#666;
  --link:#2ab0e8;
  --footer:#1c1c1c;
  --black:#000;
  --white:#fff;
}
*{margin:0;padding:0;box-sizing:border-box}
html,body{width:1200px;height:899px;overflow:hidden;background:var(--white)}
body{position:relative;font-family:"Arimo",Arial,sans-serif;color:var(--text)}

.brand{position:absolute;left:128px;top:25px;display:flex;align-items:center}
.brand-dot{width:70px;height:70px;border-radius:50%;background:var(--blue);border:4px solid #d9dbe3}
.brand-name{margin-left:10px;font-family:"Gelasio",Georgia,serif;font-size:38px;color:var(--blue);letter-spacing:.5px;margin-top:-14px}
.tagline{position:absolute;left:242px;top:77px;font-family:"Arimo",Arial,sans-serif;font-style:italic;font-size:14px;color:#333}

.search{position:absolute;left:860px;top:45px;width:209px;height:30px;border:1px solid #c8c8c8;display:flex}
.search-field{flex:1;font-size:13px;color:#999;padding:8px 12px}
.search-btn{width:35px;background:linear-gradient(#e8e8e8,#c9c9c9);border-left:1px solid #bbb}

.main-nav{position:absolute;left:538px;top:104px;width:534px;height:35px;border-radius:6px 6px 0 0;background:linear-gradient(var(--nav-top),var(--nav-bottom));display:flex;align-items:center;font-family:"Gelasio",Georgia,serif;font-weight:700;font-size:13px;color:var(--white);letter-spacing:.3px}
.main-nav a{color:inherit;text-decoration:none;text-align:center;border-right:1px solid rgba(255,255,255,.3);line-height:22px}
.main-nav a:last-child{border-right:none}
.main-nav .current{color:#0b1a40}

.band{position:absolute;left:0;width:1200px;background:var(--gray-band)}
.hero{position:absolute;left:0;top:144px;width:1200px;height:301px;background:radial-gradient(ellipse at 55% 30%,#3454b4 0%,var(--blue-hero) 55%,#1c348a 100%);overflow:hidden}
.hero-shot{position:absolute;left:133px;top:11px;width:392px;height:290px;background:linear-gradient(160deg,#f4f7fb 0%,#cfe0f3 45%,#9fbfe6 100%)}
.hero-title{position:absolute;left:610px;top:82px;font-family:"Gelasio",Georgia,serif;font-style:italic;font-size:34px;line-height:40px;color:var(--white);text-shadow:0 2px 3px rgba(0,0,0,.4)}
.hero-btn{position:absolute;top:253px;height:32px;border-radius:3px;background:linear-gradient(#fff,#e1e1e1);border:1px solid #bbb;font-family:"Gelasio",Georgia,serif;font-size:13px;color:#555;display:flex;align-items:center;justify-content:center}
.shadow{position:absolute;left:115px;top:453px;width:970px;height:26px;background:radial-gradient(ellipse at 50% 0,rgba(0,0,0,.35),rgba(0,0,0,0) 70%)}

.welcome{position:absolute;left:145px;top:508px;width:590px}
.welcome h1{font-family:"Gelasio",Georgia,serif;font-style:italic;font-weight:400;font-size:38px;color:var(--blue);margin-bottom:12px}
.welcome p{font-size:17px;line-height:20px;color:var(--text);margin-bottom:20px}

.release{position:absolute;left:752px;top:512px;width:299px;height:180px;border:2px solid #ddd;border-radius:14px;background:var(--white);box-shadow:0 2px 6px rgba(0,0,0,.2)}
.release-bar{position:absolute;left:15px;width:266px;font-family:"Gelasio",Georgia,serif;font-size:17px;display:flex;align-items:center;justify-content:center}
.release-head{top:10px;height:34px;background:#e4e4e4;color:#555}
.release-name{position:absolute;left:0;top:52px;width:100%;text-align:center;font-family:"Gelasio",Georgia,serif;font-size:30px;line-height:34px;color:var(--blue);letter-spacing:1px}
.release-link{top:142px;height:27px;background:#a9d2ee;color:var(--blue)}
.tri{display:inline-block;margin-left:7px;border-left:9px solid currentColor;border-top:5px solid transparent;border-bottom:5px solid transparent}

.footer{position:absolute;left:0;top:762px;width:1200px;height:90px;background:var(--footer)}
.footer-links{position:absolute;top:29px;left:0;width:1200px;text-align:center;font-size:14px;color:var(--link)}
.footer-links a{color:var(--link);text-decoration:none}
.copyright{position:absolute;top:49px;left:0;width:1200px;text-align:center;font-size:13px;color:#999;letter-spacing:.4px}
.social{position:absolute;left:873px;top:35px;display:flex;gap:8px}
.social span{width:27px;height:27px;border-radius:50%;background:linear-gradient(#5ec2f2,#1b7fd0)}
.base{position:absolute;left:0;top:852px;width:1200px;height:47px;background:var(--black)}
</style>
</head>
<body>
<header>
  <div class="brand"><span class="brand-dot"></span><span class="brand-name">VASTEL QUERY</span></div>
  <p class="tagline">Empowering the social science researcher</p>
  <div class="search">
    <span class="search-field">Search</span>
    <span class="search-btn">
      <svg width="35" height="28" viewBox="0 0 35 28"><circle cx="16" cy="11" r="5" fill="none" stroke="#555" stroke-width="2"/><line x1="19" y1="15" x2="22" y2="21" stroke="#555" stroke-width="3"/></svg>
    </span>
  </div>
  <nav class="main-nav">
    <a class="current" style="width:90px">HOME</a>
    <a style="width:120px">ABOUT US</a>
    <a style="width:123px">PRODUCTS</a>
    <a style="width:77px">NEWS</a>
    <a style="width:124px">CONTACT US</a>
  </nav>
</header>

<div class="band" style="top:135px;height:9px"></div>
<section class="hero">
  <div class="hero-shot" role="img" aria-label="Screenshot of the Vastel DataManager application window"></div>
  <h2 class="hero-title">Increasing the power<br>and efficiency of empirical<br>social science research</h2>
  <a class="hero-btn" style="left:713px;width:82px">Sign Up</a>
  <a class="hero-btn" style="left:804px;width:83px">Login</a>
</section>
<div class="band" style="top:445px;height:8px"></div>
<div class="shadow"></div>

<main>
  <section class="welcome">
    <h1>Welcome</h1>
    <p>The mission of Vastel Query, Inc. is to produce software products that multiply the power and efficiency of empirical scientific research in the social sciences.</p>
    <p>A central goal is to expand access to complex data sources and to the advanced methods of scientific investigation needed to analyze them.</p>
  </section>
  <aside class="release">
    <div class="release-bar release-head">Preview Release Available<span class="tri"></span></div>
    <div class="release-name">VASTEL<br>DATAMANAGER</div>
    <div class="release-bar release-link">Download Preview Release<span class="tri" style="color:#333"></span></div>
  </aside>
</main>

<div class="band" style="top:752px;height:10px"></div>
<footer class="footer">
  <div class="footer-links"><a>Privacy Policy</a> | <a>Terms of Use</a> | <a>Sitemap</a> | <a>Contact Us</a></div>
  <div class="copyright">© 2011 Vastel Query. All rights reserved.</div>
  <div class="social"><span></span><span></span><span></span></div>
</footer>
<div class="base"></div>
</body>
</html>
```